Business Card for Makeup Artist

I need a business card designed for my makeup and hair artistry business which is primarily events and weddings focused. The card needs to be sleek, simple, stylish and appealing to women. I would prefer a white background but open to suggestions also. I also love the marble background look. I have attached some example pics. It needs to be a double sided card with logo and/or design on one side and contact details in the centre of the card on the other side. NO LOGO ON BACK. Examples attached.

Target Market(s)

Females age 14-55

Industry/Entity Type

Business

Contact Information for Business Card

Nora Vint
Principal Makeup Artist
P: 0413 925 214
E: nora@lumirabeauty.com.au
W: www.lumirabeauty.com.au

Requirements
Should not have
• No yellow, green, red or blue in the design.

```html
<!DOCTYPE html>
<html lang="en">
<head>
<meta charset="utf-8">
<title>Lumira Makeup Artistry — Business Card</title>
<link rel="stylesheet" href="https://fonts.googleapis.com/css2?family=Allura&family=Jost:wght@300;400&display=swap">
<style>
  :root {
    --stage: #1f1f20;
    --card: #2b2a2b;
    --gold: #d9a86a;
    --gold-light: #f6efdc;
    --gold-mid: #e6c89c;
    --pink: #d54fb5;
    --ink: #4f4d4f;
  }
  html, body {
    margin: 0;
    width: 1200px;
    height: 750px;
    overflow: hidden;
    background: var(--stage);
  }
  .stage {
    position: relative;
    width: 1200px;
    height: 750px;
  }
  .card {
    position: absolute;
    top: 228px;
    width: 461px;
    height: 262px;
    border-radius: 11px;
    background: var(--card);
    overflow: hidden;
  }
  .card--contact { left: 124px; }
  .card--brand { left: 618px; }

  .contact {
    position: absolute;
    inset: 0;
    text-align: center;
    font-family: "Jost", sans-serif;
    font-weight: 300;
  }
  .contact__name {
    position: absolute;
    left: 0; right: 0;
    top: 70px;
    margin: 0;
    font-family: "Allura", cursive;
    font-weight: 400;
    font-size: 40px;
    line-height: 1;
    color: var(--gold);
  }
  .contact__role {
    position: absolute;
    left: 0; right: 0;
    top: 117px;
    margin: 0;
    font-size: 14px;
    color: var(--pink);
  }
  .contact__details {
    position: absolute;
    left: 0; right: 0;
    top: 153px;
    margin: 0;
    padding: 0;
    list-style: none;
    font-size: 13.5px;
    line-height: 19px;
    color: var(--gold);
  }
  .contact__details li:first-child { font-size: 14.5px; }
  .contact__rule {
    position: absolute;
    left: 142px;
    top: 222px;
    width: 177px;
    height: 1px;
    background: linear-gradient(90deg, transparent, rgba(217,168,106,.6), transparent);
  }

  .band {
    position: absolute;
    inset: 0;
    width: 461px;
    height: 262px;
  }
  .brand-name {
    position: absolute;
    left: 0;
    right: 0;
    top: 112px;
    text-align: center;
    font-family: "Jost", sans-serif;
    font-weight: 300;
    color: var(--ink);
    margin: 0;
    line-height: 1;
  }
  .brand-name__main {
    display: block;
    font-size: 34px;
    letter-spacing: 3px;
  }
  .brand-name__sub {
    display: block;
    margin-top: 4px;
    font-size: 13px;
    letter-spacing: 1px;
  }
</style>
</head>
<body>
<main class="stage">
  <section class="card card--contact">
    <div class="contact">
      <h1 class="contact__name">Nora Vint</h1>
      <p class="contact__role">Principal Makeup Artist</p>
      <ul class="contact__details">
        <li>0413 925 214</li>
        <li>nora@lumirabeauty.com.au</li>
        <li>www.lumirabeauty.com.au</li>
      </ul>
      <div class="contact__rule"></div>
    </div>
  </section>

  <section class="card card--brand">
    <svg class="band" viewBox="0 0 461 262" aria-hidden="true">
      <defs>
        <linearGradient id="gold-band" x1="0" y1="0" x2="1" y2="0">
          <stop offset="0" stop-color="#eedfc4"/>
          <stop offset="0.15" stop-color="#f7f1e2"/>
          <stop offset="0.45" stop-color="#e4c69a"/>
          <stop offset="0.75" stop-color="#f6efdc"/>
          <stop offset="1" stop-color="#e2c090"/>
        </linearGradient>
      </defs>
      <path d="M0,82 C60,100 130,102 230,84 S400,60 461,68 L461,176 C400,178 330,182 250,196 S80,214 0,172 Z" fill="url(#gold-band)"/>
    </svg>
    <p class="brand-name">
      <span class="brand-name__main">LUMIRA</span>
      <span class="brand-name__sub">MAKEUP ARTISTRY</span>
    </p>
  </section>
</main>
</body>
</html>
```